Business card and Logo for a private personal training studio

We need a business card and logo for a private personal training studio.

The studios name is "Harbour Stone Rise"
Main coloring to be a bright light blue. Looking for a crisp modern look

The front of the card is to have the

Studios name.
The Logo
Private Personal Training Studio
Kim Larden
0452 614 298

The back of the card is to have a lot of words relating to the services we offer. Please place the words vertically and horizontally using different fonts, different text sizes, different boldness and different colors to create a word picture.

Main words that need highlighting are

QVK, PILATES, BOXING, SPIN, STRENGTH, WEIGHT LOSS, BALANCE

Other words to add to the mix with less emphasis

Fitness, Conditioning, Lifestyle, Wellness, Health, Energy, Cardio, Goals, Muscle Tone, Vitality, Confidence, Attitude, Determination, Motivation, Dedication, Fun

Target Market(s)

Woman aged 30 to 60

Industry/Entity Type

Personal Trainer

Contact Information for Business Card

Harbour Stone Rise
Kim Larden
0452 614 298

Colors
0493ce
33a6d7
85cae6

```html
<!DOCTYPE html>
<html lang="en">
<head>
<meta charset="utf-8">
<title>Harbour Stone Rise – Business Card</title>
<link rel="stylesheet" href="https://fonts.googleapis.com/css2?family=Open+Sans:wght@400;600;700;800&display=swap">
<style>
  :root {
    --page-bg: #e9e9e9;
    --card-black: #0c0c0c;
    --card-black-soft: #1a1a1a;
    --brand-blue: #0493ce;
    --brand-blue-mid: #33a6d7;
    --brand-blue-light: #85cae6;
    --swoosh-grey: #d4d4d4;
    --text-white: #ffffff;
    --text-muted: #b9b9b9;
  }
  * { box-sizing: border-box; margin: 0; padding: 0; }
  html, body {
    width: 1200px;
    height: 900px;
    overflow: hidden;
    background: var(--page-bg);
    font-family: "Open Sans", Arial, sans-serif;
  }
  .canvas {
    position: relative;
    width: 1200px;
    height: 900px;
    display: flex;
    flex-direction: column;
    align-items: center;
    justify-content: center;
    gap: 44px;
  }
  .card {
    position: relative;
    width: 630px;
    height: 360px;
    overflow: hidden;
    background: radial-gradient(ellipse at 50% 30%, var(--card-black-soft), var(--card-black) 75%);
    box-shadow: 0 8px 24px rgba(0,0,0,0.25);
  }

  /* Back card: service word picture */
  .card-back { text-align: center; padding-top: 34px; }
  .wordmark {
    font-weight: 600;
    color: var(--brand-blue);
    letter-spacing: 0.06em;
    text-transform: uppercase;
  }
  .card-back .wordmark { font-size: 24px; line-height: 1; }
  .tagline {
    color: var(--text-muted);
    font-size: 8.5px;
    letter-spacing: 0.32em;
    text-transform: uppercase;
    margin-top: 5px;
  }
  .services-main {
    margin-top: 26px;
    color: var(--brand-blue);
    font-weight: 800;
    font-size: 25px;
    line-height: 1.22;
    text-transform: uppercase;
  }
  .services-extra {
    margin-top: 16px;
    color: var(--text-white);
    font-weight: 600;
    font-size: 14.5px;
    line-height: 1.75;
  }
  .dot {
    display: inline-block;
    width: 8px;
    height: 8px;
    border-radius: 50%;
    background: var(--brand-blue);
    margin: 0 7px;
    vertical-align: middle;
  }
  .services-main .dot { width: 11px; height: 11px; margin: 0 8px; }

  /* Front card: name and contact */
  .card-front .wave {
    position: absolute;
    inset: 0;
    width: 100%;
    height: 100%;
  }
  .brand-lockup {
    position: absolute;
    right: 40px;
    top: 34px;
    display: flex;
    flex-direction: column;
    align-items: flex-end;
  }
  .brand-mark {
    width: 78px;
    height: 78px;
    border-radius: 50%;
    background: var(--brand-blue);
    margin-right: 78px;
    margin-bottom: 16px;
  }
  .card-front .wordmark { font-size: 25px; line-height: 1; }
  .card-front .tagline { margin-top: 5px; }
  .contact {
    position: absolute;
    left: 44px;
    top: 196px;
  }
  .contact-name {
    color: var(--brand-blue);
    font-weight: 700;
    font-size: 22px;
  }
  .contact-phone {
    display: flex;
    align-items: center;
    gap: 8px;
    margin-top: 8px;
    color: var(--text-white);
    font-size: 16px;
  }
  .phone-icon { width: 13px; height: 13px; }
</style>
</head>
<body>
<main class="canvas">

  <section class="card card-back" aria-label="Card back">
    <div class="wordmark">Harbour Stone Rise</div>
    <div class="tagline">Private Personal Training Studio</div>
    <div class="services-main">
      <div>QVK<span class="dot"></span>Pilates<span class="dot"></span>Boxing<span class="dot"></span>Spin</div>
      <div>Strength<span class="dot"></span>Weight Loss<span class="dot"></span>Balance</div>
    </div>
    <div class="services-extra">
      <div>Fitness<span class="dot"></span>Conditioning<span class="dot"></span>Lifestyle<span class="dot"></span>Wellness<span class="dot"></span>Health</div>
      <div>Energy<span class="dot"></span>Cardio<span class="dot"></span>Goals<span class="dot"></span>Muscle Tone<span class="dot"></span>Vitality</div>
      <div>Confidence<span class="dot"></span>Attitude<span class="dot"></span>Determination</div>
      <div>Motivation<span class="dot"></span>Dedication<span class="dot"></span>Fun</div>
    </div>
  </section>

  <section class="card card-front" aria-label="Card front">
    <svg class="wave" viewBox="0 0 630 360" preserveAspectRatio="none" aria-hidden="true">
      <path d="M0,290 C160,318 330,290 470,210 C520,182 570,160 630,150 L630,360 L0,360 Z" fill="var(--brand-blue)"/>
      <path d="M0,262 C120,300 280,300 420,232 C440,222 455,212 468,204 C330,282 170,300 0,290 Z" fill="var(--swoosh-grey)"/>
      <path d="M0,290 C160,318 330,290 470,210" fill="none" stroke="var(--card-black)" stroke-width="4"/>
    </svg>
    <div class="brand-lockup">
      <div class="brand-mark"></div>
      <div class="wordmark">Harbour Stone Rise</div>
      <div class="tagline">Private Personal Training Studio</div>
    </div>
    <div class="contact">
      <div class="contact-name">Kim Larden</div>
      <div class="contact-phone">
        <svg class="phone-icon" viewBox="0 0 24 24" aria-hidden="true">
          <path fill="var(--brand-blue)" d="M6.6 10.8a15.1 15.1 0 0 0 6.6 6.6l2.2-2.2c.3-.3.7-.4 1-.2 1.1.4 2.3.6 3.6.6.6 0 1 .4 1 1V20c0 .6-.4 1-1 1A17 17 0 0 1 3 4c0-.6.4-1 1-1h3.5c.6 0 1 .4 1 1 0 1.3.2 2.5.6 3.6.1.3 0 .7-.2 1z"/>
        </svg>
        <span>0452 614 298</span>
      </div>
    </div>
  </section>

</main>
</body>
</html>
```